Resume

I am an industrial designer that has just graduated from school. I have been trying to brand myself when applying to companies. Even though I know of the basic principles in graphic design I have difficulty executing it. I have supplied my logo (which is simple but clean) and two forms of my resume I was playing around with. One is Mostly text the other has more color and is more graphic. I would like something in the middle. I would like to have a creative graph that is easy to read that displays my skills.
Updates

Project Deadline Extended
Reason: Some of the designers were asking for an extra day. I gave it 3.

Industry/Entity Type

Graphic Design

```html
<!DOCTYPE html>
<html lang="en">
<head>
<meta charset="utf-8">
<title>Owen Marsh — Industrial Designer Resume</title>
<link rel="stylesheet" href="https://fonts.googleapis.com/css2?family=PT+Sans:wght@400;700&display=swap">
<style>
  :root {
    --header-red: #ae2f26;
    --skills-band: #ad2e25;
    --education-band: #ab5040;
    --work-band: #a0505a;
    --body-text: #666666;
    --heading-text: #555555;
    --page-border: #666666;
    --white: #ffffff;
  }
  * { margin: 0; padding: 0; box-sizing: border-box; }
  html, body {
    width: 1200px; height: 1000px; overflow: hidden;
    background: var(--white);
    font-family: "PT Sans", Arial, sans-serif;
  }
  .resume-page {
    position: absolute; left: 248px; top: 55px;
    width: 686px; height: 886px;
    border: 1px solid var(--page-border);
    background: var(--white);
    overflow: hidden;
  }
  .masthead {
    position: absolute; left: 0; top: 0; width: 100%; height: 175px;
    background: var(--header-red); color: var(--white);
  }
  .name-mark {
    position: absolute; left: 30px; top: 32px; width: 142px; height: 114px;
    background: var(--white); border-radius: 10px 10px 0 10px;
    display: flex; align-items: center; justify-content: center;
    color: var(--header-red); font-size: 20px; font-weight: 400;
  }
  .contact-list { position: absolute; left: 184px; top: 52px; list-style: none; }
  .contact-list li {
    display: flex; align-items: center; height: 27px;
    font-size: 11.5px;
  }
  .contact-list svg { width: 16px; height: 16px; margin-right: 8px; fill: var(--white); }
  .identity { position: absolute; right: 34px; top: 66px; text-align: right; }
  .identity-name { font-size: 32px; font-weight: 400; line-height: 1.05; letter-spacing: .4px; }
  .identity-role { font-size: 13.5px; line-height: 1.3; }
  .section-band {
    position: absolute; left: 0; width: 100%; height: 22px;
    color: var(--white); font-size: 16px; font-weight: 400;
    text-align: center; line-height: 22px;
  }
  .band-skills { top: 183px; background: var(--skills-band); }
  .band-education { top: 472px; background: var(--education-band); }
  .band-work { top: 636px; background: var(--work-band); }
  .skills-charts { position: absolute; left: 0; top: 210px; }
  .chart-label { fill: var(--white); font-family: "PT Sans", Arial, sans-serif; font-size: 8px; letter-spacing: .3px; }
  .chart-label.large { font-size: 8.5px; }
  .entry {
    position: absolute; width: 300px;
    font-size: 11px; line-height: 13.6px; color: var(--body-text);
  }
  .entry h3 { font-size: 11px; font-weight: 700; color: var(--heading-text); white-space: nowrap; }
  .entry .gap { margin-top: 5px; }
  .entry .spaced { margin-top: 14px; }
  .col-left { left: 27px; }
  .col-right { left: 371px; }
</style>
</head>
<body>
<main class="resume-page">
  <header class="masthead">
    <div class="name-mark">Owen Marsh</div>
    <ul class="contact-list">
      <li>
        <svg viewBox="0 0 16 16" aria-hidden="true"><path d="M4 1h8a1 1 0 0 1 1 1v12a1 1 0 0 1-1 1H4a1 1 0 0 1-1-1V2a1 1 0 0 1 1-1zm1 2v8h6V3zm3 9.2a.9.9 0 1 0 0 1.8.9.9 0 0 0 0-1.8z"/></svg>
        1.555.204.7781
      </li>
      <li>
        <svg viewBox="0 0 16 16" aria-hidden="true"><path d="M1 4h14v9H1zm1 .6L8 9l6-4.4V4H2z"/></svg>
        buildwithowen@mailbox.com
      </li>
      <li>
        <svg viewBox="0 0 16 16" aria-hidden="true"><path d="M8 1.5 1 8h2v6.5h4v-4h2v4h4V8h2z"/></svg>
        folioshelf.net/omarsh
      </li>
    </ul>
    <div class="identity">
      <h1 class="identity-name">OWEN MARSH</h1>
      <p class="identity-role">INDUSTRIAL DESIGNER</p>
    </div>
  </header>

  <h2 class="section-band band-skills">SOFTWARE AND SKILLS</h2>

  <svg class="skills-charts" width="686" height="260" viewBox="0 0 686 260" role="img" aria-label="Radial charts of software and soft skills">
    <defs>
      <path id="sw-photo" d="M166 93.1A31.9 31.9 0 1 0 166 156.9A31.9 31.9 0 1 0 166 93.1"/>
      <path id="sw-render" d="M166 79.4A45.6 45.6 0 1 0 166 170.6A45.6 45.6 0 1 0 166 79.4"/>
      <path id="sw-shop" d="M166 65.7A59.3 59.3 0 1 0 166 184.3A59.3 59.3 0 1 0 166 65.7"/>
      <path id="sw-models" d="M166 52A73 73 0 1 0 166 198A73 73 0 1 0 166 52"/>
      <path id="sw-cad" d="M166 38.4A86.6 86.6 0 1 0 166 211.6A86.6 86.6 0 1 0 166 38.4"/>
      <path id="sw-layout" d="M166 24.7A100.3 100.3 0 1 0 166 225.3A100.3 100.3 0 1 0 166 24.7"/>
      <path id="sw-vector" d="M166 11A114 114 0 1 0 166 239A114 114 0 1 0 166 11"/>
      <path id="sk-creativity" d="M504 90.4A34.6 34.6 0 1 0 504 159.6A34.6 34.6 0 1 0 504 90.4"/>
      <path id="sk-teamwork" d="M504 71.2A53.8 53.8 0 1 0 504 178.8A53.8 53.8 0 1 0 504 71.2"/>
      <path id="sk-organization" d="M504 52A73 73 0 1 0 504 198A73 73 0 1 0 504 52"/>
      <path id="sk-professionalism" d="M504 32.8A92.2 92.2 0 1 0 504 217.2A92.2 92.2 0 1 0 504 32.8"/>
      <path id="sk-communication" d="M504 13.6A111.4 111.4 0 1 0 504 236.4A111.4 111.4 0 1 0 504 13.6"/>
    </defs>

    <g class="software-chart" fill="none" stroke-width="13.7">
      <circle cx="166" cy="125" r="111" pathLength="360" stroke="#d99bb6" stroke-dasharray="180 360" transform="rotate(-90 166 125)"/>
      <circle cx="166" cy="125" r="97.3" pathLength="360" stroke="#c08ca3" stroke-dasharray="245 360" transform="rotate(-90 166 125)"/>
      <circle cx="166" cy="125" r="83.6" pathLength="360" stroke="#a27c86" stroke-dasharray="285 360" transform="rotate(-90 166 125)"/>
      <circle cx="166" cy="125" r="70" pathLength="360" stroke="#9a6a70" stroke-dasharray="290 360" transform="rotate(-90 166 125)"/>
      <circle cx="166" cy="125" r="56.3" pathLength="360" stroke="#a2595a" stroke-dasharray="315 360" transform="rotate(-90 166 125)"/>
      <circle cx="166" cy="125" r="42.6" pathLength="360" stroke="#ad4a44" stroke-dasharray="325 360" transform="rotate(-90 166 125)"/>
      <circle cx="166" cy="125" r="28.9" pathLength="360" stroke="#b3302a" stroke-dasharray="360 360" transform="rotate(-90 166 125)"/>
    </g>
    <g class="chart-label">
      <text><textPath href="#sw-photo" startOffset="8.5%">PHOTO EDIT</textPath></text>
      <text><textPath href="#sw-render" startOffset="11.2%">RENDERING</textPath></text>
      <text><textPath href="#sw-shop" startOffset="14%">SHOP SKILLS</textPath></text>
      <text><textPath href="#sw-models" startOffset="20.9%">3D MODELS</textPath></text>
      <text><textPath href="#sw-cad" startOffset="22.3%">CAD MODELS</textPath></text>
      <text><textPath href="#sw-layout" startOffset="34%">LAYOUT</textPath></text>
      <text><textPath href="#sw-vector" startOffset="51%">VECTOR ART</textPath></text>
    </g>

    <g class="skills-chart" fill="none" stroke-width="19.2">
      <circle cx="504" cy="125" r="108.4" pathLength="360" stroke="#8d7275" stroke-dasharray="288 360" transform="rotate(-90 504 125)"/>
      <circle cx="504" cy="125" r="89.2" pathLength="360" stroke="#a6766c" stroke-dasharray="290 360" transform="rotate(-90 504 125)"/>
      <circle cx="504" cy="125" r="70" pathLength="360" stroke="#a5524f" stroke-dasharray="335 360" transform="rotate(-90 504 125)"/>
      <circle cx="504" cy="125" r="50.8" pathLength="360" stroke="#b14843" stroke-dasharray="330 360" transform="rotate(-90 504 125)"/>
      <circle cx="504" cy="125" r="31.6" pathLength="360" stroke="#b2281f" stroke-dasharray="345 360" transform="rotate(-90 504 125)"/>
    </g>
    <g class="chart-label large">
      <text><textPath href="#sk-creativity" startOffset="5.7%">CREATIVITY</textPath></text>
      <text><textPath href="#sk-teamwork" startOffset="9.8%">TEAMWORK</textPath></text>
      <text><textPath href="#sk-organization" startOffset="8.4%">ORGANIZATION</textPath></text>
      <text><textPath href="#sk-professionalism" startOffset="20.9%">PROFESSIONALISM</textPath></text>
      <text><textPath href="#sk-communication" startOffset="21.5%">COMMUNICATION</textPath></text>
    </g>
  </svg>

  <h2 class="section-band band-education">EDUCATION</h2>

  <section class="entry col-left" style="top:507px">
    <h3>Harborview College of Art and Design</h3>
    <p>Port Alder, Georgia</p>
    <p>September 2008 – March 2014</p>
    <p>Industrial Design B.F.A.</p>
    <p class="gap">Activities</p>
    <p>- Member of GPD (Guild of Product Designers)</p>
  </section>

  <section class="entry col-right" style="top:507px; width:255px">
    <h3>Coral Bay State College</h3>
    <p>Coral Bay, Florida</p>
    <p>September 2006 – June 2008</p>
    <p>Drafting and Design A.A.</p>
    <p class="gap">Activities and Accomplishments</p>
    <p>- Vice President of the Golf Club 2007 - 2008</p>
    <p>- 2nd place in the Lumen Center Design Showcase for 2D design 2007</p>
  </section>

  <h2 class="section-band band-work">WORK HISTORY</h2>

  <section class="entry col-left" style="top:673px; width:292px">
    <h3>Wayfarer Goods&nbsp; - &nbsp;March 2011 to August 2011</h3>
    <p>- Worked as a sales associate in a boutique shop</p>
    <p>- Duties includes maintaining inventory, cash handling, counting tills and creating closing reports.</p>
    <p>- Helped drive sales with knowledge of the products and the local area.</p>
    <h3 class="spaced">Lark Entertainment Inc.&nbsp; - &nbsp;August 2004 to January 2010</h3>
    <p>- Assistant Manager in successful Reelhouse franchise</p>
    <p>- Duties included leading a shift of up to 5 employees, ordering merchandise, loss prevention, scheduling and improving the game section of the store.</p>
    <p>- During my time here I increased the profits from games and learned how to successfully lead a team.</p>
  </section>

  <section class="entry col-right" style="top:673px; width:282px">
    <h3>Alder Furniture Outlet&nbsp; - &nbsp;August 2010 to June 2011</h3>
    <p>- Managed a sales team for a furniture retail store</p>
    <p>- Responsibilities included sales and managing the floor, inventory, scheduling, customer relations, account management, recruiting, and handling any issues that occured.</p>
    <h3 class="spaced">Internship&nbsp; - &nbsp;June 2013</h3>
    <p>Designed signs and displays for a local beer and wine distributor. Other duties included general help in the print shop as well as building and placing the point of purchase materials in stores.</p>
  </section>
</main>
</body>
</html>
```